Road Construction Company needs business cards

We would like a new business card designed for our business.

We're a road construction company based in Qld, Australia.

Can the business card please have the following information on it.

Name: Brent Malvoy
Position: General Manager
Phone: 0471 592 304
Email: Brent.malvoy@quendix.com.au
Address: 87 Harrowgate Ave, Pindarra, QLD, 4000
Website: www.quendix.com.au

Visually we'd like the card to be professional and simple.

Attached is our logo.

Our website is www.quendix.com.au

Target Market(s)

Men aged 25-60

Contact Information for Business Card

As listed in project description

Font styles to use
Serif

Requirements
Must have
• Large logo on back of card

```html
<!DOCTYPE html>
<html lang="en">
<head>
<meta charset="utf-8">
<title>Quendix Business Card</title>
<link href="https://fonts.googleapis.com/css2?family=Poppins:wght@300;400;600;700&display=swap" rel="stylesheet">
<style>
  :root {
    --brand-blue: #0f57a3;
    --ink-blue: #0d4f96;
    --accent-blue: #3a9fd9;
    --card-white: #ffffff;
    --page-bg: #ffffff;
    --label-grey: #444444;
  }
  html, body {
    margin: 0;
    padding: 0;
    width: 1200px;
    height: 1000px;
    overflow: hidden;
    background: var(--page-bg);
    font-family: "Poppins", sans-serif;
  }
  .canvas {
    position: relative;
    width: 1200px;
    height: 1000px;
  }
  .side-label {
    position: absolute;
    font-size: 21px;
    font-weight: 400;
    color: var(--label-grey);
  }
  .side-label--back { left: 815px; top: 82px; }
  .side-label--front { left: 649px; top: 476px; }

  .card {
    position: absolute;
    width: 529px;
    height: 294px;
    box-shadow: 4px 8px 14px rgba(0,0,0,0.28);
  }
  .card--back {
    left: 261px;
    top: 86px;
    background: var(--brand-blue);
  }
  .card--front {
    left: 97px;
    top: 482px;
    background: var(--card-white);
  }

  .back-wordmark {
    position: absolute;
    left: 0;
    right: 0;
    top: 128px;
    text-align: center;
    font-size: 50px;
    font-weight: 700;
    letter-spacing: 2px;
    color: var(--card-white);
    line-height: 1;
  }
  .back-website {
    position: absolute;
    left: 0;
    right: 0;
    top: 257px;
    text-align: center;
    font-size: 17px;
    font-weight: 300;
    color: var(--card-white);
  }

  .front-header {
    position: absolute;
    top: 27px;
    left: 50px;
    display: flex;
    align-items: center;
  }
  .front-wordmark {
    font-size: 21px;
    font-weight: 700;
    color: var(--ink-blue);
    letter-spacing: 1px;
    line-height: 1;
  }
  .address {
    display: flex;
    align-items: center;
    margin-left: 32px;
    font-size: 13px;
    color: var(--ink-blue);
  }
  .address svg { margin-right: 6px; }

  .person-name {
    position: absolute;
    left: 0;
    right: 0;
    top: 112px;
    text-align: center;
    font-size: 41px;
    font-weight: 600;
    color: var(--ink-blue);
    line-height: 1;
  }
  .person-title {
    position: absolute;
    left: 0;
    right: 0;
    top: 180px;
    display: flex;
    justify-content: center;
    align-items: center;
    gap: 10px;
    font-size: 22px;
    font-weight: 400;
    color: var(--accent-blue);
  }
  .contact-row {
    position: absolute;
    left: 0;
    right: 0;
    top: 241px;
    display: flex;
    justify-content: center;
    align-items: center;
    font-size: 17px;
    color: var(--ink-blue);
  }
  .contact-item {
    display: flex;
    align-items: center;
    gap: 9px;
  }
  .contact-item + .contact-item { margin-left: 12px; }
</style>
</head>
<body>
<div class="canvas">
  <div class="side-label side-label--back">Back</div>
  <div class="side-label side-label--front">Front</div>

  <section class="card card--back">
    <div class="back-wordmark">QUENDIX</div>
    <div class="back-website">www.quendix.com.au</div>
  </section>

  <section class="card card--front">
    <div class="front-header">
      <div class="front-wordmark">QUENDIX</div>
      <div class="address">
        <svg width="12" height="16" viewBox="0 0 12 16" aria-hidden="true">
          <path d="M6 0C2.7 0 0 2.6 0 5.9 0 10.3 6 16 6 16s6-5.7 6-10.1C12 2.6 9.3 0 6 0zm0 8.3a2.4 2.4 0 1 1 0-4.8 2.4 2.4 0 0 1 0 4.8z" fill="var(--ink-blue)"/>
        </svg>
        87 Harrowgate Ave, Pindarra, QLD, 4000
      </div>
    </div>

    <div class="person-name">Brent Malvoy</div>

    <div class="person-title">
      <svg width="12" height="16" viewBox="0 0 12 16" aria-hidden="true"><path d="M11 1 2 8l9 7" fill="none" stroke="var(--accent-blue)" stroke-width="3.5" stroke-linejoin="round"/></svg>
      General Manager
      <svg width="12" height="16" viewBox="0 0 12 16" aria-hidden="true"><path d="M1 1l9 7-9 7" fill="none" stroke="var(--accent-blue)" stroke-width="3.5" stroke-linejoin="round"/></svg>
    </div>

    <div class="contact-row">
      <div class="contact-item">
        <svg width="20" height="20" viewBox="0 0 24 24" aria-hidden="true">
          <path d="M6.6 10.8a15.1 15.1 0 0 0 6.6 6.6l2.2-2.2a1 1 0 0 1 1-.25 11.4 11.4 0 0 0 3.6.57 1 1 0 0 1 1 1V20a1 1 0 0 1-1 1A17 17 0 0 1 3 4a1 1 0 0 1 1-1h3.5a1 1 0 0 1 1 1c0 1.25.2 2.45.57 3.6a1 1 0 0 1-.25 1z" fill="var(--ink-blue)"/>
        </svg>
        0471 592 304
      </div>
      <div class="contact-item">
        <svg width="28" height="20" viewBox="0 0 28 20" aria-hidden="true">
          <rect x="0" y="0" width="28" height="20" rx="2" fill="var(--ink-blue)"/>
          <path d="M1.5 2 14 11.5 26.5 2" fill="none" stroke="var(--card-white)" stroke-width="2"/>
        </svg>
        Brent.malvoy@quendix.com.au
      </div>
    </div>
  </section>
</div>
</body>
</html>
```